Marigold Shore Realty business card design

Looking for an upscale and clean business card design and updated logo. I sell to a very high-end south Florida real estate market.
Target Market(s)
High-end real estate in south Florida real estate market
Industry/Entity Type
Real Estate Agent
Contact Information for Business Card
Marigold Shore Realty, Inc
738 West Penrick Ave, Suite 400/500, Fort Lauderdale, FL 33315
Tim Harlow - Broker/Owner
954-327-8846 Direct
timshomes@quillmail.net
Website: StayPenrickAv.net
Font styles to use
Other font styles liked:
- Copperplate Gothic, Georgia, etc.
Requirements
Must have
- My photo, company name, my name and title, all info stated in Details above
Nice to have
- Luxury home design element, waterfront

```html
<!DOCTYPE html>
<html lang="en">
<head>
<meta charset="utf-8">
<title>Marigold Shore Realty business card</title>
<link rel="stylesheet" href="https://fonts.googleapis.com/css2?family=Sorts+Mill+Goudy&family=Open+Sans:wght@400;600&family=Orbitron:wght@700&display=swap">
<style>
  :root {
    --backdrop: #222222;
    --paper: #ffffff;
    --ink: #111111;
    --text: #333333;
    --night: #000000;
    --marigold: #f4c531;
    --shadow: rgba(0, 0, 0, 0.55);
    --photo-light: #5a5a5a;
    --photo-dark: #2a2a2a;
  }
  * { margin: 0; padding: 0; box-sizing: border-box; }
  html, body {
    width: 1200px; height: 1199px; overflow: hidden;
    background: var(--backdrop);
  }
  .stage { position: relative; width: 1200px; height: 1199px; }
  .card {
    position: absolute; left: 170px; width: 860px; height: 491px;
    background: var(--paper);
    box-shadow: 0 14px 30px var(--shadow);
    overflow: hidden;
  }
  .card--front { top: 90px; }
  .card--back { top: 617px; }

  .brand {
    display: flex; align-items: center; gap: 18px;
    font-family: "Sorts Mill Goudy", Georgia, serif;
    color: var(--ink);
  }
  .brand__dot { border-radius: 50%; background: var(--marigold); flex: none; }
  .card--front .brand {
    position: absolute; inset: 0;
    justify-content: center; font-size: 38px;
  }
  .card--front .brand__dot { width: 64px; height: 64px; }

  .card--back .brand {
    position: absolute; left: 70px; top: 70px; font-size: 22px; gap: 12px;
  }
  .card--back .brand__dot { width: 34px; height: 34px; }

  .panel { position: absolute; inset: 0; }

  .contacts {
    position: absolute; left: 70px; top: 170px;
    list-style: none;
    font-family: "Open Sans", Arial, sans-serif;
    color: var(--text); font-size: 18px;
  }
  .contacts li {
    display: flex; align-items: center; gap: 14px; margin-bottom: 15px;
  }
  .contacts li:last-child { align-items: flex-start; }
  .contacts .icon {
    width: 26px; height: 26px; border-radius: 50%;
    background: var(--marigold); flex: none;
    display: flex; align-items: center; justify-content: center;
  }
  .contacts .address { font-size: 15px; line-height: 1.4; color: var(--ink); }

  .portrait {
    position: absolute; right: 70px; top: 120px;
    width: 130px; height: 130px; border-radius: 50%;
    background: radial-gradient(circle at 50% 38%, var(--photo-light), var(--photo-dark));
    border: 3px solid var(--marigold);
  }

  .signature { position: absolute; right: 60px; bottom: 58px; }
  .signature__name {
    font-family: "Orbitron", Arial, sans-serif; font-weight: 700;
    font-size: 24px; letter-spacing: 6px; color: var(--marigold);
  }
  .signature__title {
    font-family: "Open Sans", Arial, sans-serif;
    font-size: 15px; color: var(--paper); margin-top: 2px;
  }
</style>
</head>
<body>
<main class="stage">

  <section class="card card--front" aria-label="Card front">
    <div class="brand">
      <span class="brand__dot"></span>
      <span class="brand__name">Marigold Shore Realty, Inc</span>
    </div>
  </section>

  <section class="card card--back" aria-label="Card back">
    <svg class="panel" width="860" height="491" viewBox="0 0 860 491" aria-hidden="true">
      <polygon points="540,0 860,0 860,491 400,491 633,190" fill="var(--night)"/>
      <polygon points="758,0 806,0 400,491" fill="var(--marigold)"/>
    </svg>

    <div class="brand">
      <span class="brand__dot"></span>
      <span class="brand__name">Marigold Shore Realty, Inc</span>
    </div>

    <ul class="contacts">
      <li>
        <span class="icon"><svg width="14" height="14" viewBox="0 0 24 24"><path d="M6.6 10.8a15 15 0 0 0 6.6 6.6l2.2-2.2a1 1 0 0 1 1-.25 11.4 11.4 0 0 0 3.6.57 1 1 0 0 1 1 1V20a1 1 0 0 1-1 1A17 17 0 0 1 3 4a1 1 0 0 1 1-1h3.5a1 1 0 0 1 1 1c0 1.25.2 2.45.57 3.57a1 1 0 0 1-.25 1z" fill="#fff"/></svg></span>
        <span>954-327-8846</span>
      </li>
      <li>
        <span class="icon"><svg width="14" height="14" viewBox="0 0 24 24"><path d="M12 3 2 12h3v8h5v-5h4v5h5v-8h3z" fill="#fff"/></svg></span>
        <span>954-327-8846</span>
      </li>
      <li>
        <span class="icon"><svg width="14" height="14" viewBox="0 0 24 24"><rect x="3" y="6" width="18" height="12" fill="none" stroke="#fff" stroke-width="2"/><path d="M3 6l9 7 9-7" fill="none" stroke="#fff" stroke-width="2"/></svg></span>
        <span>timshomes@quillmail.net</span>
      </li>
      <li>
        <span class="icon"><svg width="14" height="14" viewBox="0 0 24 24"><circle cx="12" cy="12" r="9" fill="none" stroke="#fff" stroke-width="2"/><path d="M3 12h18M12 3c3 3 3 15 0 18M12 3c-3 3-3 15 0 18" fill="none" stroke="#fff" stroke-width="1.6"/></svg></span>
        <span>StayPenrickAv.net</span>
      </li>
      <li>
        <span class="icon"><svg width="14" height="14" viewBox="0 0 24 24"><path d="M12 2a7 7 0 0 0-7 7c0 5 7 13 7 13s7-8 7-13a7 7 0 0 0-7-7zm0 9.5A2.5 2.5 0 1 1 12 6.5a2.5 2.5 0 0 1 0 5z" fill="#fff"/></svg></span>
        <span class="address">738 West Penrick Ave, Suite 400/500<br>Fort Lauderdale, FL 33315</span>
      </li>
    </ul>

    <div class="portrait" role="img" aria-label="Portrait photo of broker Tim Harlow"></div>

    <div class="signature">
      <div class="signature__name">TIM HARLOW</div>
      <div class="signature__title">Broker/Owner</div>
    </div>
  </section>

</main>
</body>
</html>
```